Website home page

www.velmatra.com - a website for traditional real estate and real Estate Auctions
We need a home page.
Please disregard the colors velmatra.com is designed with. Choose any colors you have in mind. Surprise us.
Home page should have the following buttons on it:
About Me
My Listings
Property Search
Buyers/Sellers
Concierge
Contact Me

Try buttons with pictures or without pictures, again, surprise us.
The page should not display property listings.
You can use property pictures - exterior and/or interior, nature or landscape pictures as an enhancement of the page. (if it will be the case)
Themes suggestions:
-modern
-hi-tech
-elegant
surprise us
Some sites that we like:
http://www.findpinehollow.example/
http://www.housingtarwick.example/
http://www.twonorthco.example/
http://www.vividhomesagency.example/
http://www.fennteamhomes.example/

Target Market(s)

Home buyers and sellers

Industry/Entity Type

Real Estate

Requirements
Must have
• Home page should have the following buttons on it:
About Me
My Listings
Property Search
Buyers/Sellers
Concierge
Contact Me

```html
<!DOCTYPE html>
<html lang="en">
<head>
<meta charset="utf-8">
<title>Velmatra — Real Estate &amp; Auctions</title>
<link rel="stylesheet" href="https://fonts.googleapis.com/css2?family=Source+Sans+3:wght@400;600;700&display=swap">
<style>
:root{
  --bg-deep:#2a1505;
  --bg-mid:#3a1e0a;
  --header-wood:#5a3318;
  --header-wood-dark:#3e220e;
  --panel:#3b1f0a;
  --gold-light:#e2b476;
  --gold:#c98e4b;
  --gold-dark:#8a5424;
  --text-soft:#d7a77a;
  --text-body:#e0b48c;
  --logo-orange:#f3a51e;
  --nav-text:#f0d2b2;
}
*{box-sizing:border-box;margin:0;padding:0}
html,body{width:1186px;height:1200px;overflow:hidden;background:var(--bg-deep)}
body{font-family:"Source Sans 3",Arial,sans-serif;position:relative}
.page{position:relative;width:1186px;height:1200px;overflow:hidden;
  background:radial-gradient(ellipse 520px 300px at 600px 260px,#4b280f 0%,var(--bg-mid) 55%,var(--bg-deep) 100%)}
.page-backdrop{position:absolute;left:0;top:0}

/* header */
.site-header{position:absolute;left:0;top:0;width:1186px;height:95px;
  background:linear-gradient(180deg,var(--header-wood) 0%,#4d2b13 60%,var(--header-wood-dark) 100%);
  border-bottom:2px solid #1c0c02;box-shadow:0 3px 8px rgba(0,0,0,.55)}
.search-box{position:absolute;left:141px;top:35px;width:271px;height:37px;border-radius:5px;
  background:linear-gradient(180deg,#2e1707,#3a1f0b);box-shadow:inset 0 1px 3px rgba(0,0,0,.7),0 1px 0 rgba(255,220,180,.12)}
.search-box span{position:absolute;left:18px;top:9px;color:#f3e2cf;font-size:14px}
.search-box svg{position:absolute;right:10px;top:7px}
.main-nav{position:absolute;left:438px;top:35px;width:604px;height:37px;border-radius:5px;display:flex;
  background:linear-gradient(180deg,#2e1707,#3a1f0b);box-shadow:inset 0 1px 3px rgba(0,0,0,.7),0 1px 0 rgba(255,220,180,.12)}
.main-nav a{flex:auto;display:flex;align-items:center;justify-content:center;color:var(--nav-text);
  font-size:14px;text-decoration:none;border-right:1px solid #1c0c02;box-shadow:1px 0 0 rgba(255,220,180,.08)}
.main-nav a:last-child{border-right:none;box-shadow:none}

/* hero */
.hero-stage{position:absolute;left:139px;top:110px;width:903px;height:321px;
  background:linear-gradient(180deg,#45240d,#3a1e09);box-shadow:0 14px 18px -6px rgba(0,0,0,.6)}
.brand-card{position:absolute;left:258px;top:128px;width:196px;height:242px;background:#3f210b;
  transform:rotate(-10deg);box-shadow:4px 6px 14px rgba(0,0,0,.55)}
.brand-card.back{left:150px;top:140px;width:200px;height:240px;transform:rotate(4deg);background:#3a1e09}
.brand-name{position:absolute;left:284px;top:206px;font-size:44px;font-weight:700;color:var(--logo-orange);
  transform:rotate(-10deg)}
.hero-photo{position:absolute;left:510px;top:174px;width:509px;height:237px;
  background:linear-gradient(180deg,#7c4a3a 0%,#a9826c 30%,#cfc5b5 55%,#b8ad98 82%,#6b6a42 100%);
  box-shadow:0 6px 14px rgba(0,0,0,.5)}

/* gallery strip */
.gallery{position:absolute;left:139px;top:496px;width:900px;height:241px;background:var(--panel);
  border:1px solid #4b2a12;box-shadow:0 8px 16px rgba(0,0,0,.65)}
.gallery-tab{position:absolute;left:159px;top:478px;width:177px;height:36px;border-radius:4px;
  background:linear-gradient(180deg,var(--gold-light),var(--gold) 60%,var(--gold-dark));
  color:#3a1e09;font-size:17px;display:flex;align-items:center;justify-content:center;box-shadow:0 2px 4px rgba(0,0,0,.6)}
.slider-arrow{position:absolute;top:484px;width:30px;height:26px;border-radius:4px;
  background:linear-gradient(180deg,var(--gold-light),var(--gold-dark));box-shadow:0 2px 3px rgba(0,0,0,.6)}
.slider-arrow.prev{left:960px}.slider-arrow.next{left:998px}
.slider-arrow svg{display:block;margin:6px auto}
.gallery-photo{position:absolute;top:548px;width:164px;height:160px}

/* welcome */
.welcome-title{position:absolute;left:142px;top:768px;color:var(--gold);font-size:17px;font-weight:400}
.welcome-rule{position:absolute;left:142px;top:801px;width:890px;border-top:1px dotted #5a361a}
.welcome-text{position:absolute;left:146px;top:833px;width:554px;color:var(--text-body);font-size:12.6px;line-height:22px}
.welcome-photo-frame{position:absolute;left:741px;top:827px;width:293px;height:165px;border:1px solid #5a3318;padding:6px;background:#2e1707}
.welcome-photo{width:100%;height:100%;background:linear-gradient(180deg,#e7e8ea 0%,#5e6b55 35%,#6a4a30 60%,#eef0f0 80%,#e9ebeb 100%)}

/* footer */
.footer-arc{position:absolute;left:0;top:1010px}
.footer-nav{position:absolute;left:0;top:1075px;width:1150px;text-align:center;color:var(--text-soft);font-size:12px}
.footer-nav a{color:var(--text-soft);text-decoration:none;margin:0 6px}
.social{position:absolute;top:1114px;width:26px;height:26px;border-radius:50%;background:#6b3d18;box-shadow:inset 0 0 0 2px #7d4a1f}
.copyright{position:absolute;left:0;top:1163px;width:1150px;text-align:center;color:var(--text-soft);font-size:11.5px}
</style>
</head>
<body>
<div class="page">
  <svg class="page-backdrop" width="1186" height="1200" aria-hidden="true">
    <polygon points="0,560 139,490 139,431 0,470" fill="#3f210b"/>
    <polygon points="1186,520 1042,431 1042,380 1186,420" fill="#3f210b"/>
  </svg>

  <header class="site-header">
    <div class="search-box">
      <span>Search</span>
      <svg width="22" height="22" viewBox="0 0 22 22" aria-hidden="true">
        <circle cx="8" cy="8" r="6" fill="none" stroke="#6b4020" stroke-width="2.5"/>
        <line x1="12.5" y1="12.5" x2="19" y2="19" stroke="#6b4020" stroke-width="3.5" stroke-linecap="round"/>
      </svg>
    </div>
    <nav class="main-nav">
      <a href="#">About Me</a><a href="#">My Listings</a><a href="#">Property Search</a>
      <a href="#">Buyers/Sellers</a><a href="#">Concierge</a><a href="#">Contact Me</a>
    </nav>
  </header>

  <div class="hero-stage"></div>
  <div class="brand-card back"></div>
  <div class="brand-card"></div>
  <div class="brand-name">Velmatra</div>
  <div class="hero-photo" role="img" aria-label="Photo of a two-storey suburban home exterior"></div>

  <section class="gallery"></section>
  <div class="gallery-tab">Featured Property</div>
  <div class="slider-arrow prev"><svg width="10" height="14" aria-hidden="true"><path d="M7 2 L2 7 L7 12" fill="none" stroke="#2e1606" stroke-width="2.5"/></svg></div>
  <div class="slider-arrow next"><svg width="10" height="14" aria-hidden="true"><path d="M3 2 L8 7 L3 12" fill="none" stroke="#2e1606" stroke-width="2.5"/></svg></div>

  <div class="gallery-photo" style="left:159px;background:linear-gradient(180deg,#b9d3e6 0%,#9cc0dc 40%,#4a7f56 48%,#3d8ea8 56%,#2b7b96 100%)" role="img" aria-label="Landscape photo of a calm sea and island"></div>
  <div class="gallery-photo" style="left:336px;background:linear-gradient(180deg,#c9c2b4 0%,#9b7a4e 35%,#5f7f3f 65%,#3aa7b0 100%)" role="img" aria-label="Photo of a tropical garden beside a pool"></div>
  <div class="gallery-photo" style="left:513px;background:linear-gradient(180deg,#6a5038 0%,#d8cbb4 30%,#b89a78 65%,#8a4a36 100%)" role="img" aria-label="Interior photo of a bright living room"></div>
  <div class="gallery-photo" style="left:687px;background:linear-gradient(180deg,#3b6fcf 0%,#5a8ee0 30%,#c9a9a0 45%,#e4e0d8 55%,#1f5fb0 75%,#184e95 100%)" role="img" aria-label="Photo of a blue swimming pool under clear sky"></div>
  <div class="gallery-photo" style="left:860px;background:linear-gradient(90deg,#cfc4b8 0%,#b9a898 40%,#7a5a48 65%,#d9d2ca 100%)" role="img" aria-label="Interior photo of a modern hallway"></div>

  <h2 class="welcome-title">Welcome&nbsp; to our site</h2>
  <div class="welcome-rule"></div>
  <p class="welcome-text">You may place a bid as high as you want to go, but the system will raise it only as high as needed. For instance, if current bid is $100K and you place $150 the system will raise the bid only to $101K and select you as a high bidder. If someone, places a higher bid, say $120K, the system will automatically place a bid of $121K on your behalf and select you as a high bidder. However, if someone places a bid of $151K or greater this person will be selected as a high bidder.</p>
  <div class="welcome-photo-frame"><div class="welcome-photo" role="img" aria-label="Photo of a wooden house among pine trees in winter snow"></div></div>

  <svg class="footer-arc" width="1186" height="60" aria-hidden="true">
    <path d="M150 50 Q593 -20 1036 50" fill="none" stroke="#3e210b" stroke-width="3"/>
  </svg>
  <nav class="footer-nav">
    <a href="#">About Me</a>|<a href="#">My Listings</a>|<a href="#">Property Search</a>|<a href="#">Buyers/Sellers</a>|<a href="#">Concierge</a>|<a href="#">Contact Me</a>
  </nav>
  <a class="social" href="#" aria-label="Social link" style="left:512px"></a>
  <a class="social" href="#" aria-label="Social link" style="left:544px"></a>
  <a class="social" href="#" aria-label="Social link" style="left:576px"></a>
  <a class="social" href="#" aria-label="Social link" style="left:609px"></a>
  <p class="copyright">Copyrights @ 2012 All Rights Reserved</p>
</div>
</body>
</html>
```